Bring to life the sophistication and high-level expertise of my consulting business

I am looking for a sleek, modern, sharp PowerPoint design package, with options for a wide range of slide types.
We would like our logo/graphic and its colors (a blue pallet) to be prominently featured. The design should communicate expertise, sophistication, executive-level of work, be bold and look clean and sleek at the same time. There should be no doubt this was professionally done.
The font that will best work with this logo is a basic font using AvantGarde BkBt (custom)
Company briefing:
A consulting and advisory practice specialized in the Consumer Goods and Services Industries. Our methodology is distinguished by its ability to transform visionary thinking—be it blue-sky ideas, inspiration, or innovation—into practical strategies. We drive initiatives aimed at driving revenue growth and enhancing profit margins using 3 pillars: THE PEOPLE, THE CUSTOMER EXPERIENCE and THE OPERATING PLATFORM.
Target audiences are in 3 key areas: C-suite executives (owners and decision-makers of small to mid-cap companies), partners in larger Consulting Companies and Investment Firms (Private Equity/Venture capital, etc)

*In addition to the PowerPoint package, I would like a quote for designs for an email signature, a Microsoft Word template, and a company Pronetix page (all in the same style as the PPT template)

Low design quality

Target Market(s)

Target audiences are in 3 key areas: C-suite executives (owners and decision-makers), partners in larger Consulting Companies and Investment Firms (Private Equity/Venture capital, etc.)

Industry/Entity Type

Business Consulting and Advisory

Font styles to use
Sans Serif
Other font styles liked:
• The font that will work best with the logo is basic font using AvantGarde BkBt (custom)

Colors
0054AA
0677BA
7BADD7
CADEEF
E8F1F8
0094D4
00A9DD
6FCCEA
C7EBF8
E9F6FB

Requirements
Must have
• We would like our logo, the graphic shapes and its colors (a blue pallet) to be prominently featured. The design should communicate expertise, sophistication, executive-level of work. It should be sleek, modern, bold and unique.
Nice to have
• A large number of slide options for each type of slide as part of the package
Should not have
• it should not look busy, generic or too traditional

```html
<!DOCTYPE html>
<html lang="en">
<head>
<meta charset="utf-8">
<title>Veraltiq – Presentation Slides</title>
<link href="https://fonts.googleapis.com/css2?family=Jost:wght@400;500;600;700&family=Roboto:wght@400;500;700&display=swap" rel="stylesheet">
<style>
:root{
  --navy:#0054AA;
  --blue:#0677BA;
  --mid:#7BADD7;
  --pale:#CADEEF;
  --mist:#E8F1F8;
  --sky:#0094D4;
  --cyan:#00A9DD;
  --aqua:#6FCCEA;
  --ice:#C7EBF8;
  --ink:#1b1b1b;
  --grey:#6b6b6b;
  --page:#d3d3d3;
}
*{margin:0;padding:0;box-sizing:border-box}
html,body{width:1200px;height:3914px;overflow:hidden;background:var(--page)}
body{position:relative;font-family:"Roboto",Arial,sans-serif;color:var(--ink)}
.slide{position:absolute;width:981px;height:552px;background:#fff;overflow:hidden}
.footer{position:absolute;left:0;bottom:0;width:100%;height:28px;background:var(--blue);color:#fff;font-size:11.5px;display:flex;align-items:center;justify-content:center}
.footer::before{content:"";position:absolute;left:0;top:0;width:200px;height:100%;background:var(--cyan)}
.footer span{position:relative}
.heading{position:absolute;left:44px;top:33px;height:40px;padding-left:22px;font-family:"Jost",sans-serif;font-weight:700;font-size:34px;line-height:40px;letter-spacing:-.3px;color:var(--ink)}
.heading::before{content:"";position:absolute;left:0;top:0;width:7px;height:100%;background:linear-gradient(var(--cyan),var(--navy))}
.heading em{font-style:normal;color:var(--blue)}
.brand{position:absolute;display:flex;align-items:center;gap:10px;font-family:"Jost",sans-serif;font-weight:500;font-size:15px;letter-spacing:5px;color:var(--navy)}
.brand i{display:block;width:26px;height:26px;border-radius:50%;background:var(--sky)}
.slide-brand{right:42px;top:38px}
.photo{position:absolute;border-radius:50%}
/* cover */
.cover{left:114px;top:112px}
.cover-bg{position:absolute;inset:0;background:linear-gradient(100deg,#0a6cc4 0%,#0b86d4 55%,#10b6ee 100%)}
.cover-text{position:absolute;left:44px;top:100px;color:#fff}
.cover-text .welcome{font-size:14px;font-weight:500}
.cover-text h1{font-family:"Jost",sans-serif;font-weight:700;font-size:58px;letter-spacing:.5px;line-height:1;margin:20px 0 22px}
.cover-text p{font-size:17px;font-weight:700;line-height:33px}
.cover-wave{position:absolute;left:0;top:380px}
.cover-brand{left:50%;top:476px;transform:translateX(-50%);font-size:20px;letter-spacing:6px}
/* about */
.about{left:114px;top:740px}
.about h2{position:absolute;left:46px;top:168px;font-family:"Jost",sans-serif;font-weight:400;font-size:21px;letter-spacing:-.3px}
.about .body{position:absolute;left:46px;top:214px;width:448px;font-size:11.2px;line-height:19px;color:#555;text-align:justify}
.about .body p+p{margin-top:5px}
/* pillars */
.pillars{left:114px;top:1367px}
.pillar{position:absolute;left:504px;width:440px}
.pillar .icon{position:absolute;left:0;top:0;width:78px;height:78px;border-radius:50%;background:linear-gradient(160deg,var(--cyan),var(--navy))}
.pillar h3{position:absolute;left:94px;top:-6px;font-size:15px;font-weight:500}
.pillar p{position:absolute;left:94px;top:20px;width:346px;font-size:11.5px;line-height:20px;color:var(--grey)}
/* projects */
.projects{left:105px;top:1994px}
.projects-bg{position:absolute;left:0;top:0;width:100%;height:263px;background:linear-gradient(100deg,#14aee8 0%,#0b86d4 50%,#0a6cc4 100%)}
.projects h2{position:absolute;left:0;right:0;top:76px;text-align:center;font-family:"Jost",sans-serif;font-weight:600;font-size:34px;color:#fff}
.projects .rule{position:absolute;left:444px;top:130px;width:94px;height:4px;background:#fff}
.project{position:absolute;top:207px;width:280px;text-align:center}
.project .badge{width:106px;height:106px;margin:0 auto;border-radius:50%;background:var(--pale);border:4px solid #fff;display:flex;align-items:center;justify-content:center}
.project h3{margin-top:28px;font-size:19px;font-weight:700}
.project p{margin-top:6px;font-size:11.5px;line-height:19px;color:var(--grey)}
/* chart */
.chart{left:114px;top:2622px}
.chart svg.plot{position:absolute;left:0;top:0}
.bullets{position:absolute;left:668px;top:122px;width:280px;list-style:none}
.bullets li{position:relative;padding-left:23px;font-size:11.5px;line-height:19px;color:#444;margin-bottom:10px}
.bullets li::before{content:"";position:absolute;left:0;top:3px;width:12px;height:12px;border-radius:50%;background:var(--sky)}
.bullets li::after{content:"";position:absolute;left:3.5px;top:6px;width:5px;height:3px;border-left:1.6px solid #fff;border-bottom:1.6px solid #fff;transform:rotate(-45deg)}
/* team */
.team{left:109px;top:3249px}
.member{position:absolute;width:290px;height:88px}
.member .avatar{position:absolute;left:0;top:0;width:88px;height:88px;border-radius:50%;background:linear-gradient(150deg,#8a99a8,#3d4a57)}
.member h3{position:absolute;left:104px;top:22px;font-size:16px;font-weight:500}
.member p{position:absolute;left:104px;top:47px;font-size:12px;color:var(--grey)}
</style>
</head>
<body>

<!-- Cover -->
<section class="slide cover">
  <div class="cover-bg" role="img" aria-label="Business team meeting in a bright office, washed in blue"></div>
  <div class="cover-text">
    <div class="welcome">Welcome To</div>
    <h1>VERALTIQ</h1>
    <p>We are a consulting and advisory practice specialized<br>in the Consumer Goods and Services Industries.</p>
  </div>
  <svg class="cover-wave" width="981" height="172" viewBox="0 0 981 172">
    <path d="M0 110 C250 10 600 -20 981 90 L981 172 L0 172Z" fill="var(--pale)"/>
    <path d="M0 130 C260 40 620 30 981 110 L981 172 L0 172Z" fill="#fff"/>
  </svg>
  <div class="brand cover-brand"><i></i>VERALTIQ</div>
</section>

<!-- About -->
<section class="slide about">
  <div class="heading">ABOUT <em>US</em></div>
  <div class="brand slide-brand"><i></i>VERALTIQ</div>
  <h2>LOREM IPSUM DOLOR SIT</h2>
  <div class="body">
    <p>Lorem ipsum dolor sit amet, consectetur adipiscing elit, sed do eiusmod tempor incididunt ut labore et dolore magna aliqua. Ut enim ad minim veniam, quis nostrud exercitation ullamco laboris nisi ut aliquip ex ea commodo consequat. Duis aute irure dolor in reprehenderit in voluptate velit esse cillum dolore eu fugiat nulla pariatur.</p>
    <p>Sed ut perspiciatis unde omnis iste natus error sit voluptatem accusantium doloremque laudantium, totam rem aperiam, eaque ipsa quae ab illo inventore veritatis et quasi architecto beatae vitae dicta sunt explicabo.</p>
    <p>Duis aute irure dolor in reprehenderit in voluptate velit esse cillum dolore eu fugiat nulla pariatur. Excepteur sint occaecat cupidatat non proident.</p>
  </div>
  <svg style="position:absolute;left:550px;top:167px" width="386" height="386" viewBox="0 0 386 386"><circle cx="194" cy="194" r="186" fill="none" stroke="var(--blue)" stroke-width="5"/></svg>
  <div class="photo" role="img" aria-label="Two colleagues smiling across a meeting table" style="left:555px;top:170px;width:375px;height:375px;background:linear-gradient(140deg,#c9d6e4,#8ea6c0 55%,#d8c6c8)"></div>
  <div class="footer"><span>© 2024 Veraltiq | All Rights Reserved</span></div>
</section>

<!-- Pillars -->
<section class="slide pillars">
  <div class="heading">USING <em>PILLARS</em></div>
  <div class="brand slide-brand"><i></i>VERALTIQ</div>
  <svg style="position:absolute;left:42px;top:96px" width="386" height="386" viewBox="0 0 386 386"><circle cx="189" cy="193" r="187" fill="none" stroke="var(--sky)" stroke-width="5"/></svg>
  <div class="photo" role="img" aria-label="Team of four professionals gathered around a laptop" style="left:50px;top:100px;width:372px;height:372px;background:linear-gradient(140deg,#e7e5e1,#b8b1a8 55%,#5c6066)"></div>
  <div class="pillar" style="top:122px">
    <div class="icon"></div>
    <h3>The People</h3>
    <p>Sed ut perspiciatis unde omnis iste natus error sit voluptatem accusantium doloremque laudantium, totam rem aperiam, eaque ipsa quae ab illo inventore veritatis vitae dicta sunt explicabo.</p>
  </div>
  <div class="pillar" style="top:242px">
    <div class="icon"></div>
    <h3>The Customer Experience</h3>
    <p>Sed ut perspiciatis unde omnis iste natus error sit voluptatem accusantium doloremque laudantium, totam rem aperiam, eaque ipsa quae ab illo inventore veritatis vitae dicta sunt explicabo.</p>
  </div>
  <div class="pillar" style="top:363px">
    <div class="icon"></div>
    <h3>The Operating Platform</h3>
    <p>Sed ut perspiciatis unde omnis iste natus error sit voluptatem accusantium doloremque laudantium, totam rem aperiam, eaque ipsa quae ab illo inventore veritatis vitae dicta sunt explicabo.</p>
  </div>
  <div class="footer"><span>© 2024 Veraltiq | All Rights Reserved</span></div>
</section>

<!-- Projects -->
<section class="slide projects">
  <div class="projects-bg" role="img" aria-label="Office team at work, tinted in blue"></div>
  <h2>TITLE GOES HERE</h2>
  <div class="rule"></div>
  <div class="project" style="left:38px">
    <div class="badge">
      <svg width="52" height="52" viewBox="0 0 52 52" fill="none" stroke="#222" stroke-width="2"><circle cx="24" cy="28" r="20"/><circle cx="24" cy="28" r="13"/><circle cx="24" cy="28" r="6"/><path d="M24 28 L44 8 M38 8 H44 V14"/></svg>
    </div>
    <h3>Project Name</h3>
    <p>Lorem ipsum dolor sit amet, consectetur adipiscing elit, sed do eiusmod tempor incididunt ut labore et dolore magna aliqua.</p>
  </div>
  <div class="project" style="left:354px">
    <div class="badge">
      <svg width="52" height="52" viewBox="0 0 52 52" fill="none" stroke="#222" stroke-width="2"><path d="M44 8 C30 8 20 18 16 30 L22 36 C34 32 44 22 44 8Z"/><circle cx="32" cy="20" r="4"/><path d="M16 30 L8 30 L14 22 L22 22 M22 36 L22 44 L30 38 L30 30 M12 40 L6 46 M16 44 L12 48"/></svg>
    </div>
    <h3>Project Name</h3>
    <p>Lorem ipsum dolor sit amet, consectetur adipiscing elit, sed do eiusmod tempor incididunt ut labore et dolore magna aliqua.</p>
  </div>
  <div class="project" style="left:674px">
    <div class="badge">
      <svg width="52" height="52" viewBox="0 0 52 52" fill="none" stroke="#222" stroke-width="2"><rect x="4" y="6" width="36" height="28" rx="2"/><path d="M10 26 V18 M16 26 V14 M22 26 V20"/><circle cx="34" cy="34" r="9"/><path d="M40 40 L48 48"/></svg>
    </div>
    <h3>Project Name</h3>
    <p>Lorem ipsum dolor sit amet, consectetur adipiscing elit, sed do eiusmod tempor incididunt ut labore et dolore magna aliqua.</p>
  </div>
  <div class="footer"><span>© 2024 Veraltiq | All Rights Reserved</span></div>
</section>

<!-- Chart -->
<section class="slide chart">
  <div class="heading">TITLE GOES <em>HERE</em></div>
  <div class="brand slide-brand"><i></i>VERALTIQ</div>
  <svg class="plot" width="640" height="552" viewBox="0 0 640 552" font-family="Roboto, Arial, sans-serif" font-size="11" font-weight="700">
    <g stroke="#e3e3e3" stroke-width="1">
      <line x1="84" y1="122" x2="603" y2="122"/><line x1="84" y1="176" x2="603" y2="176"/>
      <line x1="84" y1="230" x2="603" y2="230"/><line x1="84" y1="285" x2="603" y2="285"/>
      <line x1="84" y1="339" x2="603" y2="339"/><line x1="84" y1="393" x2="603" y2="393"/>
      <line x1="84" y1="447" x2="603" y2="447"/>
      <line x1="84" y1="122" x2="84" y2="447"/><line x1="158" y1="122" x2="158" y2="447"/>
      <line x1="232" y1="122" x2="232" y2="447"/><line x1="306" y1="122" x2="306" y2="447"/>
      <line x1="381" y1="122" x2="381" y2="447"/><line x1="455" y1="122" x2="455" y2="447"/>
      <line x1="529" y1="122" x2="529" y2="447"/><line x1="603" y1="122" x2="603" y2="447"/>
    </g>
    <g fill="#333" text-anchor="end">
      <text x="68" y="126">120</text><text x="68" y="180">100</text><text x="68" y="234">80</text>
      <text x="68" y="289">60</text><text x="68" y="343">40</text><text x="68" y="397">20</text><text x="68" y="451">0</text>
    </g>
    <g fill="var(--blue)">
      <rect x="99" y="176" width="14" height="271"/><rect x="173" y="203" width="14" height="244"/>
      <rect x="247" y="311" width="14" height="136"/><rect x="322" y="176" width="14" height="271"/>
      <rect x="396" y="176" width="14" height="271"/><rect x="470" y="284" width="14" height="163"/>
      <rect x="544" y="311" width="14" height="136"/>
    </g>
    <g fill="var(--cyan)">
      <rect x="120" y="203" width="14" height="244"/><rect x="194" y="230" width="14" height="217"/>
      <rect x="268" y="176" width="14" height="271"/><rect x="343" y="284" width="14" height="163"/>
      <rect x="417" y="203" width="14" height="244"/><rect x="491" y="244" width="14" height="203"/>
      <rect x="565" y="176" width="14" height="271"/>
    </g>
    <g fill="#222" text-anchor="middle" font-size="10.5">
      <text x="106" y="170">100</text><text x="127" y="197">90</text>
      <text x="180" y="197">90</text><text x="201" y="224">80</text>
      <text x="254" y="305">50</text><text x="275" y="170">100</text>
      <text x="329" y="170">100</text><text x="350" y="278">60</text>
      <text x="403" y="170">100</text><text x="424" y="197">90</text>
      <text x="477" y="278">60</text><text x="498" y="238">75</text>
      <text x="551" y="305">50</text><text x="572" y="170">100</text>
    </g>
    <g fill="#333" text-anchor="middle" font-size="12">
      <text x="117" y="471">Sun</text><text x="191" y="471">Mon</text><text x="265" y="471">Tue</text>
      <text x="339" y="471">Wed</text><text x="414" y="471">Thu</text><text x="488" y="471">Fri</text><text x="562" y="471">Sat</text>
    </g>
  </svg>
  <ul class="bullets">
    <li>Lorem ipsum dolor sit consectetur adipiscing elit, sed do eiusmod tempor incididunt ut labore et dolore magna aliqua.</li>
    <li>Lorem ipsum dolor sit consectetur adipiscing elit, sed do eiusmod</li>
    <li>Lorem ipsum dolor sit consectetur adipiscing elit, sed do eiusmod tempor incididunt ut labore et dolore magna aliqua.</li>
    <li>Lorem ipsum dolor sit consectetur adipiscing elit, sed do eiusmod</li>
    <li>Lorem ipsum dolor sit consectetur adipiscing elit, sed do eiusmod tempor incididunt ut labore et dolore magna aliqua.</li>
    <li>Lorem ipsum dolor sit consectetur adipiscing elit, sed do eiusmod</li>
  </ul>
  <div class="footer"><span>© 2024 Veraltiq | All Rights Reserved</span></div>
</section>

<!-- Team -->
<section class="slide team">
  <div class="heading">THE LEADERSHIP <em>TEAM</em></div>
  <div class="brand slide-brand"><i></i>VERALTIQ</div>
  <div class="member" style="left:74px;top:128px"><div class="avatar" role="img" aria-label="Portrait photo of team member"></div><h3>OWEN HARTLEY</h3><p>Lorem ipsum</p></div>
  <div class="member" style="left:384px;top:128px"><div class="avatar" role="img" aria-label="Portrait photo of team member"></div><h3>RAVI DUMONT</h3><p>Lorem ipsum</p></div>
  <div class="member" style="left:693px;top:128px"><div class="avatar" role="img" aria-label="Portrait photo of team member"></div><h3>TESS MORROW</h3><p>Lorem ipsum</p></div>
  <div class="member" style="left:74px;top:246px"><div class="avatar" role="img" aria-label="Portrait photo of team member"></div><h3>NADIA FERRIS</h3><p>Lorem ipsum</p></div>
  <div class="member" style="left:384px;top:246px"><div class="avatar" role="img" aria-label="Portrait photo of team member"></div><h3>LEON CASTELL</h3><p>Lorem ipsum</p></div>
  <div class="member" style="left:693px;top:246px"><div class="avatar" role="img" aria-label="Portrait photo of team member"></div><h3>MAYA LINDEN</h3><p>Lorem ipsum</p></div>
  <div class="member" style="left:74px;top:368px"><div class="avatar" role="img" aria-label="Portrait photo of team member"></div><h3>CLARA VOSS</h3><p>Lorem ipsum</p></div>
  <div class="member" style="left:384px;top:368px"><div class="avatar" role="img" aria-label="Portrait photo of team member"></div><h3>IVY SANDERSON</h3><p>Lorem ipsum</p></div>
  <div class="member" style="left:693px;top:368px"><div class="avatar" role="img" aria-label="Portrait photo of team member"></div><h3>MARCUS BELL</h3><p>Lorem ipsum</p></div>
  <div class="footer"><span>© 2024 Veraltiq | All Rights Reserved</span></div>
</section>

</body>
</html>
```